Design a Website Mockup for a Job Search Engine

This design contest is for a Job Search Engine.
Similar to popular job search engines like: [login to view URL], [login to view URL], [login to view URL] and [login to view URL]
I require a modern beautiful design that is not too overpowering but blows the above sites away.
The design must be highly driven toward the perfect user experience with guidance on the correct fonts to be used and search result placement for best visibility.
The pages that i require mocked up:
Homepage, Search Results (check out [login to view URL] or [login to view URL] for the type of data that will be shown on the results page), About page
Please be creative as possible.
The winner will be the mockup that displays the best UX experience with a modern catchy design.
Please note the site will be a responsive design so please also show mockups for tablet and mobile as well as desktop for all above pages.

```html
<!DOCTYPE html>
<html lang="en">
<head>
<meta charset="utf-8">
<title>Website Name — Jobs</title>
<link href="https://fonts.googleapis.com/css2?family=Raleway:wght@400;500;600;700;800&display=swap" rel="stylesheet">
<style>
:root{
  --blue:#1fa9dd;
  --green:#2da44a;
  --green-dark:#258c3e;
  --ink:#333a40;
  --muted:#7d8388;
  --line:#e6e6e6;
  --soft:#f7f7f7;
  --white:#ffffff;
}
*{box-sizing:border-box;margin:0;padding:0}
html,body{width:1200px;height:2400px;overflow:hidden;background:var(--white)}
body{font-family:'Raleway',sans-serif;color:var(--ink);position:relative}
.abs{position:absolute}
a{color:inherit;text-decoration:none}

/* hero */
.hero{left:0;top:0;width:1200px;height:437px;background:linear-gradient(180deg,#3c4043 0%,#2e3134 45%,#45494c 100%)}
.logo{left:161px;top:33px;color:var(--white);font-weight:800;font-size:21px;letter-spacing:.3px}
.nav{right:161px;top:39px;display:flex;gap:22px;color:var(--white);font-size:12px;font-weight:700}
.nav span{display:flex;align-items:center;gap:6px}
.hero-title{left:0;width:1200px;top:126px;text-align:center;color:var(--white);font-size:32px;font-weight:400;line-height:41px}
.hero-title b{font-weight:700}
.hero-rule{left:550px;top:233px;width:100px;height:3px;background:#d9d9d9}
.search-label{top:298px;color:var(--white);font-size:13px;font-weight:700}
.search{left:257px;top:324px;width:684px;height:45px;display:flex}
.search .field{background:var(--white);height:45px;display:flex;align-items:center;padding-left:20px;font-size:10.5px;color:#9aa0a4}
.search .field+.field{border-left:1px solid var(--line)}
.search .go{width:68px;background:var(--blue);display:flex;align-items:center;justify-content:center}

/* quick links */
.quick{left:0;top:437px;width:1200px;height:110px;background:var(--green)}
.quick ul{position:absolute;left:161px;top:0;width:878px;height:110px;display:flex;list-style:none;border-left:1px solid rgba(255,255,255,.15)}
.quick li{flex:1;display:flex;flex-direction:column;align-items:center;justify-content:center;gap:14px;color:var(--white);font-size:12.5px;font-weight:700;border-right:1px solid rgba(255,255,255,.15)}
.quick li.active{background:var(--green-dark)}
.quick li svg{height:36px}

/* headings */
.section-title{left:0;width:1200px;text-align:center;font-size:17.5px;font-weight:700;color:var(--ink)}
.section-rule{left:573px;width:54px;height:3px;background:var(--blue)}

/* solutions */
.solutions{left:187px;top:700px;width:825px;height:295px;border:1px solid var(--line);display:flex}
.solution{flex:1;background:var(--soft);text-align:center;padding-top:53px}
.solution+.solution{background:var(--white);border-left:1px solid var(--line)}
.solution h3{font-size:34px;font-weight:700;line-height:40px}
.seekers h3{color:var(--blue)}
.employers h3{color:var(--green)}
.solution p{margin:18px auto 0;width:345px;font-size:12px;line-height:19px;color:#666}
.btn{display:inline-flex;align-items:center;justify-content:center;color:var(--white);font-size:13.5px;font-weight:400}
.solution .btn{margin-top:26px;width:163px;height:50px}
.bg-blue{background:var(--blue)}
.bg-green{background:var(--green)}

/* categories */
.categories{left:161px;top:1144px;width:878px;display:flex}
.categories ul{list-style:none;width:219.5px}
.categories li{font-size:11px;color:#8a9095;height:26.3px;display:flex;align-items:center;gap:9px}
.categories li::before{content:"";width:5px;height:5px;border-right:1.5px solid var(--blue);border-top:1.5px solid var(--blue);transform:rotate(45deg)}

/* testimonials */
.testimonial{left:0;top:1372px;width:1200px;height:325px;background:linear-gradient(90deg,#4a4541 0%,#5a534d 35%,#534c46 65%,#403b38 100%)}
.testimonial h2{position:absolute;left:0;width:1200px;top:73px;text-align:center;color:var(--white);font-size:17.5px;font-weight:700}
.testimonial blockquote{position:absolute;left:255px;width:690px;top:150px;text-align:center;color:#f0f0f0;font-size:14px;line-height:22.5px}
.testimonial cite{position:absolute;left:0;width:1200px;top:236px;text-align:center;font-size:14px;font-style:normal;color:var(--white)}
.testimonial cite b{font-style:italic;font-weight:700}
.testimonial cite span{color:var(--blue)}
.arrow{top:130px}

/* guarantee */
.badge{left:161px;top:1753px;width:168px;height:168px}
.promise{left:380px;top:1777px;width:660px;font-size:13.5px;line-height:23px;color:#666}
.register{left:380px;top:1844px;display:flex;align-items:center}
.register strong{font-size:13px;font-weight:700;width:139px}
.register .btn{width:177px;height:49px;margin-right:16px}

/* footer */
.footer{left:0;top:1977px;width:1200px;height:326px;background:var(--soft);border-bottom:1px solid var(--line)}
.footer-cols{position:absolute;left:161px;top:66px;width:878px;display:flex}
.footer-col{width:219.5px}
.footer-col h4{font-size:18px;font-weight:700;color:var(--ink);margin-bottom:17px}
.footer-col ul{list-style:none}
.footer-col li{font-size:11px;color:#8a9095;height:22.5px}
.subscribe p{font-size:11px;line-height:19px;color:#8a9095;text-align:center;margin-top:-2px}
.subscribe .email{margin-top:18px;height:40px;background:var(--white);border:1px solid var(--line);display:flex;align-items:center;justify-content:center;font-size:10.5px;color:#b0b5b8}
.subscribe .btn{margin-top:12px;width:220px;height:38px}
.copyright{left:0;width:1200px;top:2343px;text-align:center;font-size:10.5px;color:#777}
</style>
</head>
<body>

<header class="hero abs" role="img" aria-label="Blurred photo of business people walking through a bright office lobby"></header>
<div class="logo abs">WEBSITE NAME</div>
<nav class="nav abs">
  <span><svg width="12" height="12" viewBox="0 0 12 12"><circle cx="6" cy="3.5" r="3" fill="#fff"/><path d="M0 12c0-4 3-5.5 6-5.5S12 8 12 12z" fill="#fff"/></svg>REGISTER</span>
  <span><svg width="13" height="12" viewBox="0 0 13 12" fill="none" stroke="#fff" stroke-width="1.5"><path d="M7 1h5v10H7"/><path d="M1 6h7M5 3l3 3-3 3"/></svg>LOGIN</span>
  <span><svg width="12" height="12" viewBox="0 0 12 12" fill="none" stroke="#fff" stroke-width="1.4"><rect x="1" y="2" width="8" height="9"/><path d="M5 7l6-6"/></svg>POST YOUR JOB</span>
  <span><svg width="12" height="12" viewBox="0 0 12 12" fill="none" stroke="#fff" stroke-width="1.7"><circle cx="4.5" cy="4.5" r="3.5"/><path d="M7 7l4.5 4.5"/></svg>VIEW JOBS</span>
</nav>
<h1 class="hero-title abs">We all about <b>Jobs</b> and getting candidates and<br>employers the <b>Right Fit</b> at the <b>Right Time</b>!</h1>
<div class="hero-rule abs"></div>
<div class="search-label abs" style="left:257px">WHAT DO YOU WANT TO DO?</div>
<div class="search-label abs" style="left:573px">WHERE ARE YOU LOOKING?</div>
<form class="search abs">
  <div class="field" style="width:316px">Job, Title, Skills, or Company</div>
  <div class="field" style="width:300px">City, State, or Zip</div>
  <div class="go"><svg width="28" height="28" viewBox="0 0 28 28" fill="none" stroke="#fff" stroke-width="2.4"><circle cx="12" cy="12" r="9"/><path d="M19 19l7 7"/></svg></div>
</form>

<section class="quick abs">
  <ul>
    <li><svg viewBox="0 0 28 34" width="29"><rect x="2" y="2" width="24" height="30" fill="none" stroke="#fff" stroke-width="2.5"/><circle cx="14" cy="12" r="4" fill="#fff"/><rect x="8" y="18" width="12" height="3" fill="#fff"/><rect x="7" y="25" width="14" height="2" fill="#fff"/></svg>CURRENT OPENINGS</li>
    <li class="active"><svg viewBox="0 0 30 36" width="30"><path d="M2 2h16l6 6v12" fill="none" stroke="#fff" stroke-width="2.5"/><path d="M2 2v30h12" fill="none" stroke="#fff" stroke-width="2.5"/><rect x="6" y="11" width="12" height="2.5" fill="#fff"/><rect x="6" y="17" width="10" height="2.5" fill="#fff"/><circle cx="22" cy="27" r="7" fill="#fff"/><path d="M18.5 27l2.5 2.5 4.5-5" fill="none" stroke="#258c3e" stroke-width="2"/></svg>APPLY</li>
    <li><svg viewBox="0 0 36 36" width="36"><path d="M4 4h18v28H4z" fill="none" stroke="#fff" stroke-width="2.5"/><path d="M8 11h10M8 17h10M8 23h6" stroke="#fff" stroke-width="2"/><path d="M30 6l4 4-12 14-5 1 1-5z" fill="#fff"/></svg>BLOGS</li>
    <li><svg viewBox="0 0 42 32" width="42"><circle cx="10" cy="10" r="5" fill="#fff"/><circle cx="32" cy="10" r="5" fill="#fff"/><circle cx="21" cy="9" r="7" fill="#fff"/><path d="M1 28c0-7 4-10 9-10s7 2 7 2M41 28c0-7-4-10-9-10s-7 2-7 2" fill="#fff"/><path d="M9 32c0-9 6-13 12-13s12 4 12 13z" fill="#fff"/></svg>MEET OUR TEAM</li>
  </ul>
</section>

<h2 class="section-title abs" style="top:611px">OUR SOLUTIONS THAT WORK FOR YOU</h2>
<div class="section-rule abs" style="top:644px"></div>

<section class="solutions abs">
  <div class="solution seekers">
    <h3>JOB SEEKERS</h3>
    <p>Lorem ipsum dolor sit amet, consectetur adipiscing elit. Phasellus diam augue, luctus et imperdiet scelerisque, vehicula nec sem.</p>
    <a class="btn bg-blue">READ MORE</a>
  </div>
  <div class="solution employers">
    <h3>EMPLOYERS</h3>
    <p>Lorem ipsum dolor sit amet, consectetur adipiscing elit. Phasellus diam augue, luctus et imperdiet scelerisque, vehicula nec sem.</p>
    <a class="btn bg-green">READ MORE</a>
  </div>
</section>

<h2 class="section-title abs" style="top:1057px">FIND JOBS BY CATEGORY</h2>
<div class="section-rule abs" style="top:1090px"></div>

<section class="categories abs">
  <ul><li>Part-Time</li><li>Office &amp; Admin</li><li>General Management</li><li>High Tech</li><li>Business &amp; Finance</li><li>Health Professionals</li></ul>
  <ul><li>Healthcare Support</li><li>Sales</li><li>Media &amp; Entertainment</li><li>Personal Care</li><li>Engineering &amp; Architecture</li><li>Transportation</li></ul>
  <ul><li>Education &amp; Training</li><li>Social Services</li><li>Science</li><li>Trades</li><li>Repair &amp; Installation</li><li>Legal</li></ul>
  <ul><li>Restaurant &amp; Food Service</li><li>Protection</li><li>Construction</li><li>Building Maintenance</li><li>Agriculture</li><li>Military</li></ul>
</section>

<section class="testimonial abs" role="img" aria-label="Dimmed group photo of smiling colleagues behind the testimonial">
  <h2>WHAY PEOPLE SAY</h2>
  <blockquote>Lorem ipsum dolor sit amet, consectetur adipiscing elit. Phasellus diam augue, luctus et imperdiet scelerisque, vehicula nec sem. Nunc ante nisl, rutrum at pharetra quis, consequat dictum leo. Quisque rutrum, quam tempor sagittis ultricies, turpis lectus laoreet ante.</blockquote>
  <cite><b>Smith Doe,</b> <span>Mechanical Engineer</span></cite>
  <svg class="abs arrow" style="left:161px" width="20" height="44" viewBox="0 0 20 44" fill="none" stroke="#bbb" stroke-width="2"><path d="M18 2L2 22l16 20"/></svg>
  <svg class="abs arrow" style="left:1019px" width="20" height="44" viewBox="0 0 20 44" fill="none" stroke="#bbb" stroke-width="2"><path d="M2 2l16 20L2 42"/></svg>
</section>

<svg class="badge abs" viewBox="0 0 168 168"><circle cx="84" cy="84" r="82" fill="var(--blue)"/></svg>
<p class="promise abs">We are commited to quality, speed and exceptional customer service! But we will not rest until you're happy. If for any reason you're not satisfied with our service, we'll give you 100% of your money back</p>
<div class="register abs">
  <strong>REGISTER NOW!</strong>
  <a class="btn bg-blue">AS A CANDIDATE</a>
  <a class="btn bg-green">AS AN EMPLOYER</a>
</div>

<footer class="footer abs">
  <div class="footer-cols">
    <div class="footer-col"><h4>INFORMATION</h4><ul><li>About Us</li><li>Terms &amp; Conditions</li><li>Privacy Policy</li><li>Resources</li><li>Career with Us</li><li>Sitemap</li><li>Contact Us</li></ul></div>
    <div class="footer-col"><h4>JOB SEEKERS</h4><ul><li>Resume Writing</li><li>Profile Enhancement</li><li>Recruiter Reach</li><li>Jobs For You</li><li>Jobs By Company</li><li>Jobs By Category</li><li>Jobs By Destination</li></ul></div>
    <div class="footer-col"><h4>EMPLOYERS</h4><ul><li>Post Jobs</li><li>Access Database</li><li>Manage Resources</li><li>Buy Online</li><li>Report a Problem</li><li>Recruiter From World</li><li>Membership Plan</li></ul></div>
    <div class="footer-col subscribe"><h4>SUBSCRIBE JOB ALERTS</h4>
      <p>Lorem ipsum dolor sit amet, consectetur<br>adipiscing elit. Phasellus diam augue.</p>
      <div class="email">Email Address</div>
      <a class="btn bg-blue">SUBSCRIBE NOW</a>
    </div>
  </div>
</footer>
<p class="copyright abs">2015 © Copyright, Website Name, All Rights Reserved</p>

</body>
</html>
```